Harbor Oak Works business cards

I’d like a business card design that includes my logo, a tag line and my contact info. Black, textured background. My contact info color should match the orange and blue gradients. Tagline under logo: “Wooden Tables and Furniture of the Highest Quality”

Target Market(s)

High end furniture buyers

Contact Information for Business Card

Contact info, logo and tagline

```html
<!DOCTYPE html>
<html lang="en">
<head>
<meta charset="utf-8">
<title>Harbor Oak Works business cards</title>
<link href="https://fonts.googleapis.com/css2?family=Poppins:wght@400;500;600;700&display=swap" rel="stylesheet">
<style>
  :root{
    --stage:#2b2b2d;
    --card:#1c1c1e;
    --card-edge:#111113;
    --orange:#f07a22;
    --blue:#1a5bb5;
    --text:#e6e6e6;
    --muted:#bdbdbd;
    --divider:#4a4a4e;
  }
  *{box-sizing:border-box;margin:0;padding:0}
  html,body{width:1200px;height:688px;overflow:hidden}
  body{background:var(--stage);font-family:"Poppins",sans-serif;position:relative}

  .card{position:absolute;top:190px;width:540px;height:308px;border-radius:16px;
        background:var(--card);overflow:hidden;box-shadow:0 10px 30px rgba(0,0,0,.45)}
  .card--back{left:40px}
  .card--front{left:620px}

  .pattern{position:absolute;inset:0;
        background:linear-gradient(35deg,#141416 0%,#2a2a2c 55%,#4a4a4c 100%)}
  .wordmark{position:absolute;font-weight:600;color:var(--orange);white-space:nowrap;
        display:flex;align-items:center;gap:8px}
  .wordmark .dot{width:12px;height:12px;border-radius:50%;background:var(--orange)}
  .card--back .wordmark{left:50%;top:50%;transform:translate(-50%,-50%);font-size:34px}
  .card--front .wordmark{left:34px;top:112px;font-size:25px}

  .divider{position:absolute;left:282px;top:34px;width:1px;height:170px;background:var(--divider)}

  .contact{position:absolute;left:300px;top:40px;width:220px;color:var(--text)}
  .contact__name{font-size:21px;font-weight:700;line-height:1.1}
  .contact__name .first{color:var(--orange)}
  .contact__name .last{color:var(--blue)}
  .contact__role{font-size:12px;color:var(--muted);margin-bottom:12px}
  .contact__list{list-style:none;font-size:11px;line-height:1.35}
  .contact__list li{display:flex;gap:7px;align-items:flex-start;margin-bottom:2px}
  .contact__list svg{flex:none;width:11px;height:11px;margin-top:2px;fill:var(--orange)}
  .contact__list .addr{margin-top:8px}

  .tree-mark{position:absolute;right:46px;bottom:42px;width:50px;height:50px;border-radius:4px;
        background:radial-gradient(circle at 50% 40%,#c0601c,#1c1c1e 72%)}
  .band{position:absolute;left:0;bottom:0;width:100%;height:42px;background:var(--orange);
        display:flex;align-items:center;padding-left:26px;color:#fff;font-weight:600;font-size:14.5px}
  .band__accent{position:absolute;right:0;top:-22px;width:38px;height:64px;background:var(--blue)}
</style>
</head>
<body>
  <section class="card card--back" aria-label="Card back">
    <div class="pattern" role="img" aria-label="Repeating pattern of bare tree silhouettes fading from white to black"></div>
    <div class="wordmark"><span class="dot"></span>Harbor Oak Works</div>
  </section>

  <section class="card card--front" aria-label="Card front">
    <div class="wordmark"><span class="dot"></span>Harbor Oak Works</div>
    <div class="divider"></div>

    <div class="contact">
      <p class="contact__name"><span class="first">Marcus</span> <span class="last">Hale</span></p>
      <p class="contact__role">Managing Director</p>
      <ul class="contact__list">
        <li><svg viewBox="0 0 24 24"><path d="M6.6 10.8a15.1 15.1 0 0 0 6.6 6.6l2.2-2.2a1 1 0 0 1 1-.25 11.4 11.4 0 0 0 3.6.57 1 1 0 0 1 1 1V20a1 1 0 0 1-1 1A17 17 0 0 1 3 4a1 1 0 0 1 1-1h3.5a1 1 0 0 1 1 1c0 1.25.2 2.45.57 3.57a1 1 0 0 1-.25 1z"/></svg>041-555 270 318</li>
        <li><svg viewBox="0 0 24 24"><path d="M2 5h20v14H2zm2 2v.5l8 5 8-5V7l-8 5z"/></svg>hello@harboroak.net</li>
        <li><svg viewBox="0 0 24 24"><circle cx="12" cy="12" r="10"/></svg>www.harboroak.net</li>
        <li class="addr"><svg viewBox="0 0 24 24"><path d="M12 2a7 7 0 0 0-7 7c0 5 7 13 7 13s7-8 7-13a7 7 0 0 0-7-7zm0 9.5A2.5 2.5 0 1 1 12 6.5a2.5 2.5 0 0 1 0 5z"/></svg><span>48, Quay Lane<br>Seaport City, 204518</span></li>
      </ul>
    </div>

    <div class="tree-mark" role="img" aria-label="Small orange bare tree illustration"></div>
    <div class="band">
      Wooden Tables and Furniture of the Highest Quality
      <span class="band__accent"></span>
    </div>
  </section>
</body>
</html>
```